Business Card Design for a Personal Trainer

I need a business card design for my job as a personal trainer. It should have a unique, modern and exclusive design. On the front there should be only my logo with my name and my job. 0163/2918374 Tobias Kellinger Lindenfeldweg 14 80412 Munich Germany The most important contact information is the web adress. it can be bigger than the rest, but its not necessary. The card should be 8,5cmx5,5cm big. Font: Roboto. Colors: black, white, gray, 56c1ff.

```html
<!DOCTYPE html>
<html lang="de">
<head>
<meta charset="utf-8">
<title>Tobias Kellinger – Personal Trainer Visitenkarte</title>
<link href="https://fonts.googleapis.com/css2?family=Roboto:wght@300;400&family=Libre+Baskerville&display=swap" rel="stylesheet">
<style>
  :root {
    --page: #d9d5cf;
    --card-edge: #bdbdbd;
    --card-dark: #050505;
    --card-mid: #2b2b2b;
    --card-light: #4a4a4a;
    --silver: #e6e6e6;
    --text: #d4d4d4;
    --accent: #2fb3c2;
  }
  * { margin: 0; padding: 0; box-sizing: border-box; }
  html, body {
    width: 1200px; height: 969px; overflow: hidden;
    background: var(--page);
  }
  .card {
    position: absolute; left: 100px; top: 161px;
    width: 1000px; height: 647px;
    border: 2px solid var(--card-edge);
    background:
      radial-gradient(ellipse 420px 460px at 420px 250px, var(--card-light) 0%, var(--card-mid) 45%, transparent 80%),
      linear-gradient(90deg, #1c1c1c 0%, #2a2a2a 40%, var(--card-dark) 70%, var(--card-dark) 100%);
    overflow: hidden;
    font-family: "Roboto", Arial, sans-serif;
  }
  .brand {
    position: absolute; left: 240px; top: 180px; width: 406px;
    text-align: center; color: var(--silver);
  }
  .brand-name {
    display: flex; align-items: center; justify-content: center; gap: 12px;
    font-size: 40px; font-weight: 400; line-height: 1; letter-spacing: 0.5px;
  }
  .brand-mark { width: 14px; height: 14px; background: var(--silver); }
  .brand-role {
    display: flex; align-items: center; gap: 8px; margin-top: 8px;
    font-size: 17px; font-weight: 400; letter-spacing: 4.5px;
  }
  .brand-role::before, .brand-role::after {
    content: ""; flex: 1; height: 2px; background: var(--silver);
  }
  .holder {
    position: absolute; left: 42px; top: 300px;
    display: flex; align-items: flex-end; width: 525px;
    font-family: "Libre Baskerville", Georgia, serif;
    font-size: 31px; letter-spacing: 2px; color: var(--text);
  }
  .holder::after {
    content: ""; flex: 1; height: 2px; background: var(--text); margin-bottom: 6px;
  }
  .website {
    position: absolute; left: 42px; top: 362px;
    font-size: 29px; font-weight: 300; letter-spacing: 1.5px; color: var(--accent);
  }
  .contact { position: absolute; left: 44px; top: 427px; list-style: none; }
  .contact li {
    display: flex; align-items: center; gap: 16px; height: 38px;
    font-size: 25px; font-weight: 300; letter-spacing: 1px; color: var(--text);
  }
  .contact li:last-child { margin-top: 4px; }
  .contact svg { width: 24px; height: 24px; fill: var(--text); }
  .portrait {
    position: absolute; left: 652px; top: 32px; width: 320px; height: 615px;
    border-radius: 110px 110px 0 0;
    background: radial-gradient(ellipse at 50% 35%, #6a6a6a 0%, #3a3a3a 45%, #151515 90%);
  }
</style>
</head>
<body>
  <section class="card">
    <div class="brand">
      <div class="brand-name"><span class="brand-mark"></span>TOBIAS KELLINGER</div>
      <div class="brand-role">PERSONAL TRAINER</div>
    </div>

    <div class="holder">Tobias Kellinger</div>
    <div class="website">www.tobiaskellinger.de</div>

    <ul class="contact">
      <li>
        <svg viewBox="0 0 24 24" aria-hidden="true"><path d="M3 9c0-3 4-5 9-5s9 2 9 5v2h-5V8.5C14.5 8 9.5 8 8 8.5V11H3z M6 12h12l2 8H4z M12 14a2.5 2.5 0 1 0 0.01 0z"/></svg>
        0163/2918374
      </li>
      <li>
        <svg viewBox="0 0 24 24" aria-hidden="true"><path d="M3 10l9-6 9 6v10H3z M6 9h12v4l-6 3-6-3z"/></svg>
        t.kellinger@postfach-mail.de
      </li>
      <li>
        <svg viewBox="0 0 24 24" aria-hidden="true"><path d="M12 3l10 9h-3v9h-5v-6h-4v6H5v-9H2z"/></svg>
        Lindenfeldweg 14,80412 München
      </li>
    </ul>

    <div class="portrait" role="img" aria-label="Schwarz-weiß-Porträt des Personal Trainers mit verschränkten Armen im dunklen Longsleeve"></div>
  </section>
</body>
</html>
```